Dental Office Needs- Flyer Design for Same Day Crowns

We need a flyer that will explain the benefits of the same day crown from the patient prospective. Not show pictures of the machine that makes the crowns. See attached material for content. The flyer should use the practices PMS colors of Green 562 and Blue 3025. The ad should say to the patient - I want to go this office and get my crown done there.
Updates

Project Deadline Extended Reason: The difference in the time zone between USA and Europe has caused issues. Minor changes still need to be worked out. Added Thursday, July 14, 2016

Target Market(s)

Dental Patients

Industry/Entity Type

Dental

Requirements
Must have
• Call to Action
• Business Address and Business Logo
• Classic Design
• images of a Happy 50 year old Couple
• Gives the benefits of the same day crown
Should not have
• No Images of tooth figures
• No before or after pictures

```html
<!DOCTYPE html>
<html lang="en">
<head>
<meta charset="utf-8">
<title>Brookfield Dental Care – Same-Day Crowns</title>
<link href="https://fonts.googleapis.com/css2?family=Barlow:wght@300;400;500;600&family=Lato:wght@400&display=swap" rel="stylesheet">
<style>
  :root {
    --teal: #13897a;
    --teal-dark: #0f7a6c;
    --blue: #0c5b85;
    --lime: #8dc63f;
    --ink: #1f1f1f;
    --body-grey: #5e5e5e;
    --rule: #d8d8d8;
    --paper: #ffffff;
  }
  * { margin: 0; padding: 0; box-sizing: border-box; }
  html, body { width: 858px; height: 1200px; overflow: hidden; background: var(--paper); }
  .flyer {
    position: relative; width: 858px; height: 1200px; overflow: hidden;
    background: var(--paper); font-family: "Barlow", sans-serif; color: var(--ink);
  }
  .hero-art { position: absolute; left: 0; top: 0; }

  .brand { position: absolute; left: 46px; top: 96px; }
  .brand-name { font-family: "Lato", sans-serif; font-size: 29px; color: var(--blue); font-weight: 400; }
  .brand-tagline { font-family: "Lato", sans-serif; font-size: 15px; color: var(--teal); margin-top: 4px; }

  .perks { position: absolute; left: 46px; top: 219px; list-style: none; }
  .perks li { display: flex; align-items: center; height: 35px; font-size: 15.5px; letter-spacing: 0.3px; }
  .perks svg { width: 14px; height: 14px; margin-right: 17px; }

  .perks-rule { position: absolute; left: 45px; top: 322px; width: 363px; height: 1px; background: var(--rule); }
  .intro { position: absolute; left: 46px; top: 337px; width: 380px; font-family: "Lato", sans-serif; font-size: 16.5px; line-height: 25px; color: #333; }

  .visits { position: absolute; left: 46px; top: 440px; display: flex; align-items: flex-end; }
  .visits-num { font-size: 62px; font-weight: 300; color: var(--teal); line-height: 56px; }
  .visits-tag {
    background: var(--teal); color: #fff; font-weight: 500; font-size: 23px;
    height: 34px; line-height: 34px; padding: 0 24px 0 14px; margin-left: 4px; margin-bottom: 0;
    clip-path: polygon(0 0, 84% 0, 100% 100%, 0 100%);
  }
  .visits-text { font-size: 25px; margin-left: 10px; line-height: 26px; }

  .headline-rule { position: absolute; left: 46px; top: 503px; width: 764px; height: 1px; background: var(--rule); }
  .headline { position: absolute; left: 44px; top: 508px; font-size: 87px; font-weight: 300; letter-spacing: -0.5px; line-height: 90px; white-space: nowrap; }

  .band { position: absolute; right: 48px; color: #fff; font-weight: 500; text-align: right; padding-right: 12px; letter-spacing: 0.6px; }
  .band-lime { top: 603px; width: 536px; height: 44px; line-height: 44px; font-size: 24px; background: var(--lime); clip-path: polygon(0 0, 100% 0, 100% 100%, 6% 100%); }
  .band-blue { top: 649px; width: 318px; height: 45px; line-height: 45px; font-size: 30px; background: var(--blue); clip-path: polygon(0 0, 100% 0, 100% 100%, 14% 100%); }

  .couple { position: absolute; left: 44px; top: 684px; width: 320px; height: 424px; }

  .benefits { position: absolute; left: 396px; top: 728px; width: 420px; }
  .benefits-line { position: absolute; left: 5px; top: 16px; height: 246px; border-left: 1.5px dotted #9aa; }
  .benefit { position: relative; padding-left: 44px; margin-bottom: 24px; }
  .benefit::before { content: ""; position: absolute; left: 0; top: 6px; width: 13px; height: 13px; border-radius: 50%; background: var(--blue); }
  .benefit h2 { font-size: 20.5px; font-weight: 500; letter-spacing: 0.3px; margin-bottom: 7px; }
  .benefit p { font-size: 17px; line-height: 24px; color: var(--body-grey); letter-spacing: 0.3px; }
  .benefit em { font-style: normal; font-weight: 600; color: var(--teal); }

  .footer {
    position: absolute; left: 0; top: 1108px; width: 858px; height: 92px; background: var(--teal);
    clip-path: polygon(44px 0, 812px 0, 858px 100%, 0 100%);
  }
  .address { position: absolute; left: 58px; top: 1134px; display: flex; color: #fff; font-size: 17.5px; line-height: 24px; letter-spacing: 0.4px; }
  .address svg { width: 14px; height: 18px; margin: 3px 12px 0 0; }
  .contact-box {
    position: absolute; top: 1133px; width: 250px; height: 46px; border: 1.5px solid #fff; border-radius: 3px;
    display: flex; align-items: center; justify-content: center; color: #fff; font-size: 29px; letter-spacing: 0.8px;
  }
  .contact-box svg { width: 26px; height: 26px; margin-right: 8px; }
  .contact-phone { left: 272px; }
  .contact-fax { left: 550px; }
</style>
</head>
<body>
<main class="flyer">
  <svg class="hero-art" width="858" height="500" viewBox="0 0 858 500">
    <defs>
      <radialGradient id="heroGlow" cx="0.3" cy="0.7" r="0.8">
        <stop offset="0" stop-color="#f4f4f4"/>
        <stop offset="1" stop-color="#ffffff"/>
      </radialGradient>
      <linearGradient id="portraitTone" x1="0" y1="0" x2="1" y2="1">
        <stop offset="0" stop-color="#d9d9d9"/>
        <stop offset="0.5" stop-color="#9a9a9a"/>
        <stop offset="1" stop-color="#5a5a5a"/>
      </linearGradient>
      <clipPath id="portraitClip"><circle cx="880" cy="120" r="375"/></clipPath>
    </defs>
    <circle cx="900" cy="80" r="500" fill="url(#heroGlow)"/>
    <g clip-path="url(#portraitClip)">
      <rect x="480" y="0" width="378" height="500" fill="url(#portraitTone)" role="img" aria-label="Black and white portrait of a smiling young woman with long hair"/>
      <path d="M520 372 Q650 400 858 430 L858 500 L520 500 Z" fill="var(--teal)"/>
      <path d="M770 470 L858 370 L858 500 Z" fill="var(--blue)"/>
    </g>
  </svg>

  <header class="brand">
    <div class="brand-name">Brookfield Dental Care</div>
    <div class="brand-tagline">It All Begins With a Healthy Smile!</div>
  </header>

  <ul class="perks">
    <li><svg viewBox="0 0 14 14"><circle cx="7" cy="7" r="7" fill="var(--teal)"/><path d="M3.8 7.2 6 9.3 10.2 4.9" stroke="#fff" stroke-width="1.8" fill="none"/></svg>GOOD-BYE TEMPORARY CROWN</li>
    <li><svg viewBox="0 0 14 14"><circle cx="7" cy="7" r="7" fill="var(--teal)"/><path d="M3.8 7.2 6 9.3 10.2 4.9" stroke="#fff" stroke-width="1.8" fill="none"/></svg>GOOD-BYE SECOND APPOINTMENT</li>
    <li><svg viewBox="0 0 14 14"><circle cx="7" cy="7" r="7" fill="var(--teal)"/><path d="M3.8 7.2 6 9.3 10.2 4.9" stroke="#fff" stroke-width="1.8" fill="none"/></svg>GOOD-BYE GOOEY MESSY IMPRESSIONS</li>
  </ul>
  <div class="perks-rule"></div>
  <p class="intro">When it comes to your next crown, the benefits of a Digital Restoration add up quickly!</p>

  <div class="visits">
    <span class="visits-num">2</span>
    <span class="visits-tag">Hours</span>
    <span class="visits-text">Instate of 2 Visits...</span>
  </div>
  <div class="headline-rule"></div>
  <h1 class="headline">ARE YOU READY FOR</h1>
  <div class="band band-lime">A dramatically improved experience with</div>
  <div class="band band-blue">your next crown?</div>

  <div class="couple" role="img" aria-label="Black and white photo of a happy older couple standing with arms crossed" style="background: linear-gradient(160deg, #cfcfcf 0%, #8a8a8a 55%, #3c3c3c 100%);"></div>

  <section class="benefits">
    <div class="benefits-line"></div>
    <article class="benefit">
      <h2>A Same-Day Restoration</h2>
      <p>We understand how <em>hard</em> it can be to take off work or have someone take care of the kids even once, but <em>twice??</em></p>
    </article>
    <article class="benefit">
      <h2>A Stronger More Precise Fit</h2>
      <p>Brookfield Dental Care is pleased to offer you the <em>Comfort</em> and <em>Convenience</em> of One Visit Dental Care.</p>
    </article>
    <article class="benefit">
      <h2>A Beautiful Natural Appearance</h2>
      <p>Now with <em>3D CADCAM</em> Technology, we can digitally design and mill a Customized, Ceramic Restoration in one appointment.</p>
    </article>
  </section>

  <footer class="footer"></footer>
  <div class="address">
    <svg viewBox="0 0 14 18"><path d="M7 0C3.1 0 0 3 0 6.8 0 11.5 7 18 7 18s7-6.5 7-11.2C14 3 10.9 0 7 0Zm0 9.5a2.7 2.7 0 1 1 0-5.4 2.7 2.7 0 0 1 0 5.4Z" fill="#fff"/></svg>
    <div>418 E. Lakeview Rd.<br>Lakeview, MI 48102</div>
  </div>
  <div class="contact-box contact-phone">
    <svg viewBox="0 0 26 26"><circle cx="13" cy="13" r="11.5" stroke="#fff" stroke-width="1.8" fill="none"/><path d="M9 7.5c.6-.5 1.3-.4 1.6.2l1 2c.2.5.1 1-.3 1.3l-.8.6c.6 1.5 1.7 2.7 3.2 3.4l.7-.8c.4-.4.9-.5 1.4-.2l1.9 1.1c.6.3.7 1 .2 1.6l-1 1c-.8.8-2.2.9-3.6.2-2.7-1.4-4.6-3.5-5.6-6.1-.5-1.4-.3-2.6.3-3.3Z" fill="#fff"/></svg>
    555.310.2247
  </div>
  <div class="contact-box contact-fax">
    <svg viewBox="0 0 26 26"><rect x="7" y="3" width="12" height="6" fill="#fff"/><rect x="2" y="10" width="22" height="10" rx="2" fill="#fff"/><rect x="7" y="16" width="12" height="8" fill="#fff" stroke="var(--teal)" stroke-width="1.5"/><circle cx="20" cy="13" r="1.2" fill="var(--teal)"/></svg>
    555.310.2248
  </div>
</main>
</body>
</html>
```